Vantrel Web Services

This is a new It services company operating in Perth western Australia

we need a website that is easy to navigate without a cluttered feel to it it should have the following links and pages

About Us
Services
Clients
Contact Us
MY Vantrel (login for clients)

Hi it is a web based IT services company so we would expect customers to come to the website for 2 different purposes the first is to enquire about our services and then as they become customers come to our website to manage their services so whilst they are seperate we want do not want it to look like 2 different websites

hope this helps

Hi to update this we need a home page and templates for sub pages

this is a design brief only and not the coding of the pages or building of the site

```html
<!DOCTYPE html>
<html lang="en">
<head>
<meta charset="utf-8">
<title>Vantrel Web Services</title>
<link href="https://fonts.googleapis.com/css2?family=Open+Sans:wght@400;600&family=Crimson+Text&display=swap" rel="stylesheet">
<style>
:root{
  --red:#b3161b;
  --red-dark:#8e0e12;
  --ink:#2b2b2b;
  --muted:#9a9a9a;
  --line:#e6e6e6;
  --soft:#f5f6f8;
  --blue:#36a9d8;
  --icon:#9b9b9b;
  --footer:#323335;
  --footer-bottom:#262628;
  --white:#fff;
}
*{margin:0;padding:0;box-sizing:border-box}
html,body{width:717px;height:1200px;overflow:hidden}
body{font-family:"Open Sans",Arial,sans-serif;color:var(--ink);background:var(--white);position:relative}
.abs{position:absolute}

/* header */
.site-header{position:absolute;left:0;top:0;width:717px;height:58px;background:rgba(235,235,235,.93);z-index:3}
.brand{position:absolute;left:66px;top:15px;display:flex;align-items:center;gap:8px}
.brand-dot{width:28px;height:28px;border-radius:50%;background:var(--red)}
.brand-name{font-size:20px;font-weight:600;color:var(--red);letter-spacing:1px}
.main-nav{position:absolute;right:82px;top:20px;display:flex;align-items:center;gap:14px;font-size:10px;color:#222}
.login-btn{background:var(--red-dark);color:var(--white);font-weight:600;padding:5px 9px;font-size:9px}

/* hero */
.hero{position:absolute;left:0;top:0;width:717px;height:350px;background:linear-gradient(120deg,#2d2d2f 0%,#4a4a4c 40%,#262628 70%,#3a3a3c 100%)}
.hero-title{position:absolute;top:114px;width:100%;text-align:center;color:var(--white);font-size:25px;line-height:31px;font-weight:400}
.hero-text{position:absolute;top:183px;width:100%;text-align:center;color:#bfbfbf;font-size:8.5px;line-height:13px}
.hero-actions{position:absolute;top:223px;left:263px;display:flex;gap:11px}
.btn-ghost{width:92px;height:25px;border:1px solid var(--white);color:var(--white);font-size:9.5px;display:flex;align-items:center;justify-content:center}
.btn-red{width:93px;height:25px;background:var(--red);color:var(--white);font-size:9.5px;display:flex;align-items:center;justify-content:center}

/* collaborate */
.collab{position:absolute;top:350px;left:0;width:717px;height:185px;background:#f7f7f8;border-bottom:1px solid var(--line)}
.collab h2{position:absolute;left:66px;top:37px;font-size:14px;font-weight:600;line-height:20px;color:#333}
.collab p{position:absolute;left:66px;top:80px;width:220px;font-size:7.6px;line-height:12px;color:#666}
.collab .link{position:absolute;left:67px;top:132px;font-size:8px;color:var(--blue);text-decoration:underline}
.device-mock{position:absolute;left:284px;top:292px;width:364px;height:210px;border-radius:8px;background:linear-gradient(180deg,#1f1f20 0%,#e9edf1 12%,#dde3e8 88%,#bfc3c7 100%);z-index:2}

/* services */
.section-title{position:absolute;width:100%;text-align:center;font-size:14px;font-weight:600;color:#333}
.section-sub{position:absolute;width:100%;text-align:center;font-size:8.5px;color:var(--muted)}
.service-card{position:absolute;top:614px;width:138px;height:172px;border:1px solid #ececec;text-align:center}
.service-card.active{border-color:#aee0f2}
.service-card svg{position:absolute;left:39px;top:16px}
.service-card h3{position:absolute;top:85px;width:100%;font-size:10px;font-weight:400;color:#444}
.service-card p{position:absolute;top:105px;left:8px;right:8px;font-size:7.4px;line-height:12px;color:var(--muted)}
.card-btn{position:absolute;left:33px;top:147px;width:73px;height:22px;background:#eee;border:1px solid #ddd;font-size:8px;color:#444;display:flex;align-items:center;justify-content:center}
.active .card-btn{background:var(--white);border-color:var(--blue);color:var(--blue)}

/* testimonials */
.testimonials{position:absolute;top:825px;left:0;width:717px;height:226px;background:var(--soft);border-top:1px solid var(--line)}
.quote{position:absolute;top:84px;width:173px;height:47px;background:var(--white);box-shadow:0 1px 3px rgba(0,0,0,.15);font-size:7.4px;line-height:12px;color:var(--muted);padding:10px 8px}
.quote::after{content:"";position:absolute;left:22px;bottom:-8px;border-left:8px solid var(--white);border-bottom:8px solid transparent}
.author{position:absolute;top:147px;display:flex;align-items:center;gap:10px;font-size:7.4px;color:var(--muted)}
.avatar{width:29px;height:29px;border-radius:50%;background:#b9a89a}
.author b{font-weight:400;color:var(--red)}
.dots{position:absolute;top:192px;left:348px;display:flex;gap:2px}
.dots span{width:6px;height:6px;border-radius:50%;background:#ccc}
.dots span:first-child{background:var(--blue)}

/* footer */
.site-footer{position:absolute;top:1051px;left:0;width:717px;height:114px;background:var(--footer)}
.signup-text{position:absolute;left:66px;top:39px;font-size:9.5px;color:#ddd}
.signup-input{position:absolute;left:66px;top:54px;width:260px;height:21px;background:var(--white);font-family:"Crimson Text",Georgia,serif;font-size:11px;color:#999;padding:2px 4px}
.signup-btn{position:absolute;left:333px;top:54px;width:65px;height:21px;background:var(--red);color:var(--white);font-size:9.5px;font-weight:600;display:flex;align-items:center;justify-content:center}
.social{position:absolute;left:472px;top:57px;display:flex;gap:20px;align-items:center}
.social .sq{width:19px;height:19px;background:#eee;border-radius:2px}
.bottom-bar{position:absolute;top:1165px;left:0;width:717px;height:35px;background:var(--footer-bottom);font-size:7.6px;color:#aaa}
.bottom-bar .copy{position:absolute;left:66px;top:12px}
.bottom-bar .legal{position:absolute;right:65px;top:12px}
</style>
</head>
<body>

<section class="hero" role="img" aria-label="Photo of a desk with coffee cup and glasses, person working on a laptop">
  <h1 class="hero-title">Welcome To VANTREL<br>Newely Founded Online Media &amp; IT-Services</h1>
  <p class="hero-text">Lorem ipsum dolor sit amet, consectetur adipisicing elit, sed do eiusmod tempor incididunt ut labore et dolore magna aliqua.<br>Ut enim ad minim veniam, quis nostrud exercitation ullamco laboris nisi ut aliquip ex ea commodo consequat.</p>
  <div class="hero-actions"><span class="btn-ghost">Get Started Now</span><span class="btn-red">Enroll Now</span></div>
</section>

<header class="site-header">
  <div class="brand"><span class="brand-dot"></span><span class="brand-name">Vantrel</span></div>
  <nav class="main-nav">
    <span>Home</span><span>About Us</span><span>Services</span><span>Clients</span><span>Contact Us</span>
    <span class="login-btn">MY Vantrel Login</span>
  </nav>
</header>

<section class="collab">
  <h2>Enjoy The Way You<br>Work And Collaborate!</h2>
  <p>Lorem ipsum dolor sit amet, consectetur adipisicing elit, sed do eiusmod tempor incididunt ut labore et dolore magna aliqua. Ut enim ad minim veniam, quis nostrud exercitation ullamco laboris nisi ut aliquip ex ea commodo consequat.</p>
  <span class="link">Learn More</span>
</section>
<div class="device-mock" role="img" aria-label="Laptop and phone showing the client portal activity stream"></div>

<section class="services">
  <h2 class="section-title" style="top:555px">We Do IT-Services</h2>
  <p class="section-sub" style="top:580px">Lorem ipsum dolor sit amet consectetur adipsicing elit. Sed do euismod</p>

  <article class="service-card active" style="left:66px">
    <svg width="60" height="54" viewBox="0 0 60 54" fill="#8fd3ef">
      <rect x="2" y="4" width="30" height="22" rx="3" fill="none" stroke="#8fd3ef" stroke-width="4"/>
      <rect x="24" y="16" width="30" height="22" rx="3" fill="#fff" stroke="#8fd3ef" stroke-width="4"/>
      <path d="M4 32h22l3 8H0z"/><path d="M26 44h28l4 8H22z"/>
    </svg>
    <h3>System Administration</h3>
    <p>Lorem ipsum dolor sit amet consectetur adipsicing elit. Sed do Euismod tempor</p>
    <span class="card-btn">Learn More</span>
  </article>

  <article class="service-card" style="left:215px">
    <svg width="60" height="54" viewBox="0 0 60 54" fill="var(--icon)">
      <ellipse cx="30" cy="8" rx="22" ry="7"/>
      <path d="M8 13c0 4 10 7 22 7s22-3 22-7v9c0 4-10 7-22 7S8 26 8 22z"/>
      <path d="M8 27c0 4 10 7 22 7s22-3 22-7v9c0 4-10 7-22 7S8 40 8 36z"/>
      <path d="M8 41c0 4 10 7 22 7s22-3 22-7v5c0 4-10 7-22 7S8 50 8 46z"/>
    </svg>
    <h3>Database Administration</h3>
    <p>Lorem ipsum dolor sit amet consectetur adipsicing elit. Sed do Euismod tempor</p>
    <span class="card-btn">Learn More</span>
  </article>

  <article class="service-card" style="left:365px">
    <svg width="64" height="54" viewBox="0 0 64 54" fill="none" stroke="var(--icon)" stroke-width="4">
      <rect x="2" y="2" width="60" height="50"/><line x1="2" y1="12" x2="62" y2="12"/>
      <path d="M24 22l-8 9 8 9M40 22l8 9-8 9M35 20l-6 22"/>
    </svg>
    <h3>Programming</h3>
    <p>Lorem ipsum dolor sit amet consectetur adipsicing elit. Sed do Euismod tempor</p>
    <span class="card-btn">Learn More</span>
  </article>

  <article class="service-card" style="left:514px">
    <svg width="62" height="54" viewBox="0 0 62 54" fill="var(--icon)">
      <rect x="2" y="2" width="44" height="12" rx="2"/><rect x="2" y="18" width="30" height="12" rx="2"/><rect x="2" y="34" width="30" height="12" rx="2"/>
      <circle cx="46" cy="36" r="13"/><circle cx="46" cy="36" r="5" fill="#fff"/>
    </svg>
    <h3>Database &amp; Query Tunning</h3>
    <p>Lorem ipsum dolor sit amet consectetur adipsicing elit. Sed do Euismod tempor</p>
    <span class="card-btn">Learn More</span>
  </article>
</section>

<section class="testimonials">
  <h2 class="section-title" style="top:18px">What our customer says</h2>
  <p class="section-sub" style="top:44px">Lorem ipsum dolor sit amet consectetur adipsicing elit. Sed do euismod</p>
  <div class="quote" style="left:70px">Lorem ipsum dolor sit amet consectetur adip-sicing elit..</div>
  <div class="quote" style="left:272px">Lorem ipsum dolor sit amet consectetur adip-sicing elit..</div>
  <div class="quote" style="left:474px">Lorem ipsum dolor sit amet consectetur adip-sicing elit..</div>
  <div class="author" style="left:77px"><span class="avatar" role="img" aria-label="Customer portrait"></span><span>SEO specialist, <b>@Marlon Keats</b></span></div>
  <div class="author" style="left:279px"><span class="avatar" role="img" aria-label="Customer portrait"></span><span>SEO specialist, <b>@Tessa Morrow</b></span></div>
  <div class="author" style="left:481px"><span class="avatar" role="img" aria-label="Customer portrait"></span><span>SEO specialist, <b>@Dane Holloway</b></span></div>
  <div class="dots"><span></span><span></span><span></span></div>
</section>

<footer class="site-footer">
  <p class="signup-text">Join 8,000 Smart Owners Who Get Our Emails Every Month. Be Better In 2014.</p>
  <div class="signup-input">name@example.com</div>
  <span class="signup-btn">SUBCRIBE</span>
  <div class="social">
    <svg width="14" height="22" viewBox="0 0 14 22" fill="none" stroke="#eee" stroke-width="2"><rect x="1" y="1" width="12" height="20" rx="2"/><line x1="1" y1="16" x2="13" y2="16"/></svg>
    <span class="sq"></span><span class="sq"></span><span class="sq"></span>
    <svg width="22" height="18" viewBox="0 0 22 18" fill="none" stroke="#eee" stroke-width="2"><rect x="1" y="1" width="20" height="16"/><path d="M1 1l10 9 10-9M1 17l7-7M21 17l-7-7"/></svg>
  </div>
</footer>
<div class="bottom-bar">
  <span class="copy">Copyrights © 2014 Vantrelweb.com - All Rights Reserved</span>
  <span class="legal">Privacy Policy &nbsp; | &nbsp; Term &amp; Conditions</span>
</div>

</body>
</html>
```